Stationery design for a Saas platform at PR industry

Hello, Corvanta is a media database and press release distribution platform targeting Public Relations agencies and corporates. We started at Turkey and moved our HQ to San Francisco, US. We changed our website and need a new stationary design with compatible of the hew website. Our website address is http://www.corvanta-example.com/en
Updates
Reason: The number of the designers are not enough for us. Looking for some other good designs.
Industry/Entity Type
Industry
Requirements
Must have
- Statinery covers business card design, letterhead, envalope, file and invoice design.

```html
<!DOCTYPE html>
<html lang="en">
<head>
<meta charset="utf-8">
<title>Corvanta Business Card</title>
<link rel="stylesheet" href="https://fonts.googleapis.com/css2?family=Open+Sans:wght@400;600;700&display=swap">
<style>
  :root {
    --page-bg: #e9e7e4;
    --card-dark: #0f0f10;
    --card-mid: #2b2b2d;
    --card-frost: #d8d5d1;
    --frost-ring: rgba(255,255,255,0.35);
    --name-color: #d9dde6;
    --text-light: #ececec;
    --icon-color: #e2e2e2;
    --brand-ink: #141414;
  }
  * { margin: 0; padding: 0; box-sizing: border-box; }
  html, body {
    width: 1200px; height: 969px; overflow: hidden;
    background: var(--page-bg);
    font-family: "Open Sans", Arial, sans-serif;
  }
  .business-card {
    position: absolute;
    left: 120px; top: 211px;
    width: 960px; height: 546px;
    border-radius: 24px;
    overflow: hidden;
    background: linear-gradient(90deg,
      var(--card-dark) 0%, var(--card-mid) 38%, #4a4948 48%,
      #b9b6b2 60%, var(--card-frost) 70%, #e3e0dc 100%);
    box-shadow: 0 18px 40px rgba(0,0,0,0.18);
  }
  .frost-disc {
    position: absolute;
    left: 412px; top: 8px;
    width: 530px; height: 530px;
    border-radius: 50%;
    background: radial-gradient(circle at 45% 40%, rgba(255,255,255,0.28), rgba(255,255,255,0.08) 70%);
    border: 3px solid var(--frost-ring);
  }
  .contact-block {
    position: absolute;
    left: 68px; top: 98px;
    color: var(--text-light);
  }
  .person-name {
    font-size: 33px; font-weight: 700;
    color: var(--name-color);
    letter-spacing: 0.5px; line-height: 40px;
  }
  .person-role {
    font-size: 25px; font-weight: 400; line-height: 34px;
    margin-bottom: 22px;
  }
  .address-line { font-size: 24px; line-height: 31px; }
  .contact-list { list-style: none; margin-top: 20px; }
  .contact-list li {
    display: flex; align-items: center;
    font-size: 24px; line-height: 37.5px;
  }
  .contact-icon {
    width: 24px; height: 24px; margin-right: 15px;
    fill: var(--icon-color);
  }
  .brand-name {
    position: absolute;
    left: 540px; top: 222px;
    font-size: 68px; font-weight: 600;
    color: var(--brand-ink);
    letter-spacing: -0.5px; line-height: 84px;
  }
</style>
</head>
<body>
  <div class="business-card">
    <div class="frost-disc"></div>

    <div class="contact-block">
      <h1 class="person-name">DANIEL REYES</h1>
      <p class="person-role">CEO&amp;Founder</p>
      <p class="address-line">2913 Willow Crest Lane</p>
      <p class="address-line">Bellingham, Washington 98226</p>
      <ul class="contact-list">
        <li>
          <svg class="contact-icon" viewBox="0 0 24 24"><path d="M6.6 10.8a15.1 15.1 0 0 0 6.6 6.6l2.2-2.2c.3-.3.7-.4 1-.2 1.1.4 2.3.6 3.6.6.6 0 1 .4 1 1V20c0 .6-.4 1-1 1A17 17 0 0 1 3 4c0-.6.4-1 1-1h3.5c.6 0 1 .4 1 1 0 1.3.2 2.5.6 3.6.1.3 0 .7-.2 1z"/></svg>
          555.210.4471
        </li>
        <li>
          <svg class="contact-icon" viewBox="0 0 24 24"><path d="M7 1h10a2 2 0 0 1 2 2v18a2 2 0 0 1-2 2H7a2 2 0 0 1-2-2V3a2 2 0 0 1 2-2zm0 3v14h10V4zm5 15.5a1 1 0 1 0 0 2 1 1 0 0 0 0-2z"/></svg>
          555.318.6025
        </li>
        <li>
          <svg class="contact-icon" viewBox="0 0 24 24"><path d="M6 2h12v5H6zM3 8h18a2 2 0 0 1 2 2v7h-4v5H5v-5H1v-7a2 2 0 0 1 2-2zm4 8v4h10v-4z"/></svg>
          555.427.9130
        </li>
        <li>
          <svg class="contact-icon" viewBox="0 0 24 24"><path d="M2 5h20v14H2zm2 2v.5l8 5 8-5V7zm0 2.8V17h16V9.8l-8 5z"/></svg>
          dreyes@corvanta-example.com
        </li>
        <li>
          <svg class="contact-icon" viewBox="0 0 24 24"><path d="M12 2a10 10 0 1 0 0 20 10 10 0 0 0 0-20zm-1 17.9A8 8 0 0 1 4.2 10L9 14.8v1a2 2 0 0 0 2 2zm6.9-2.5A2 2 0 0 0 16 16h-1v-3a1 1 0 0 0-1-1H8v-2h2a1 1 0 0 0 1-1V7h2a2 2 0 0 0 2-2v-.4a8 8 0 0 1 2.9 12.8z"/></svg>
          www.corvanta-example.com
        </li>
      </ul>
    </div>

    <div class="brand-name">corvanta</div>
  </div>
</body>
</html>
```